Social media app sign-up flow that asks users to give personal info and connect with other apps

Design an interactive, fun, and playful sign-up flow in which you are providing information about you, your interests, and connecting with different API plug-ins such as Fendora, WorkLoop, Tunevo, etc. (using the brand palette attached).

Basic wireframe, and business requirements are also attached.

Target Market(s)

Gen Z + Millennials (ages 22-40)

Font styles to use
Sans Serif

Colors
fbed22
fbee3d
fbf289

Requirements
Must have
• Forms for users to submit their info. Follow the color palette attached.

Connect with Fendora, Connect with WorkLoop, Connect with Tunevo, Connect with Gatherwick buttons
Nice to have
• I like the way you can use cards to submit your information for each category. Interactive card design for providing your info
Should not have
• Basic outdated designs, long forms

```html
<!DOCTYPE html>
<html lang="en">
<head>
<meta charset="utf-8">
<title>Sign-Up Flow Screens</title>
<link rel="stylesheet" href="https://fonts.googleapis.com/css2?family=Jost:wght@400;500;600&display=swap">
<style>
:root{
  --backdrop:#767676;
  --screen:#2b2d33;
  --footer:#1f2126;
  --line:#5a5d66;
  --white:#ffffff;
  --muted:#a7a9ae;
  --yellow-top:#ffd84d;
  --yellow-bottom:#ffb41c;
  --card-ink:#3b2c0c;
  --caption:#f7d98a;
  --fendora:#4a62a8;
  --workloop:#0a78b8;
  --tunevo:#22b957;
  --accent:#ffc62e;
}
*{box-sizing:border-box;margin:0;padding:0}
html,body{width:1200px;height:2332px;overflow:hidden}
body{background:var(--backdrop);font-family:"Jost",sans-serif;color:var(--white);position:relative}
.screen{position:absolute;width:410px;background:var(--screen);border-radius:34px;overflow:hidden}
.abs{position:absolute}
.title{position:absolute;left:0;right:0;text-align:center;font-size:29px;font-weight:600}
.nav-back,.nav-gear{position:absolute;width:22px;height:22px}
.footer{position:absolute;left:0;right:0;bottom:0;background:var(--footer);display:flex;align-items:center;justify-content:center;font-size:20px}
.field-group{position:absolute;left:24px;width:363px;border:1px solid var(--line);border-radius:3px}
.field{padding:0 18px;height:57px;display:flex;flex-direction:column;justify-content:center;font-size:18px}
.field+.field{border-top:1px solid var(--line)}
.field small{font-size:14px;color:var(--muted)}
.primary-btn{position:absolute;left:24px;width:363px;height:53px;background:var(--accent);border-radius:3px;color:#222;font-weight:600;font-size:22px;display:flex;align-items:center;justify-content:center}
.or{position:absolute;left:0;right:0;text-align:center;font-size:13px;color:var(--muted)}
.outline-btn{position:absolute;left:24px;width:363px;height:57px;border:1px solid #7c7f88;border-radius:3px;display:flex;align-items:center;justify-content:center;gap:10px;font-size:19.5px}
.dot{width:20px;height:20px;border-radius:50%;display:inline-block}
.login-line{position:absolute;left:0;right:0;text-align:center;font-size:19px}
.login-line a{color:var(--accent)}
.card{position:absolute;width:173px;height:155px;background:linear-gradient(180deg,var(--yellow-top),var(--yellow-bottom));border-radius:3px;color:var(--card-ink);display:flex;flex-direction:column;align-items:center;justify-content:center;text-align:center;font-size:22px;font-weight:500;line-height:1.15}
.card svg{width:42px;height:42px;margin-bottom:12px}
.tile{position:absolute;border-radius:3px;overflow:hidden;color:var(--card-ink);font-weight:500;font-size:22px}
.tile-photo{position:absolute;inset:0;background:linear-gradient(160deg,#ffd44a,#ffb62a)}
.tile-label{position:absolute;inset:0;display:flex;align-items:center;justify-content:center;text-align:center;line-height:1.15}
.caption{position:absolute;left:0;right:0;bottom:0;background:var(--caption);display:flex;align-items:center;padding-left:13px;font-size:17px}
.connect-btn{position:absolute;left:24px;width:363px;height:57px;border-radius:3px;display:flex;align-items:center;justify-content:center;gap:10px;font-weight:600;font-size:19.5px}
</style>
</head>
<body>

<!-- Screen 1: sign up -->
<section class="screen" style="left:133px;top:162px;height:908px">
  <h1 class="title" style="top:50px">New Sign-Up Flow</h1>
  <div class="field-group" style="top:117px">
    <div class="field" style="height:71px;position:relative">
      <small>Country/Region</small>United States(+1)
      <svg class="abs" style="right:18px;top:26px" width="30" height="16" viewBox="0 0 30 16"><path d="M1 1l14 13L29 1" fill="none" stroke="#fff" stroke-width="2"/></svg>
    </div>
    <div class="field">Phone Number</div>
  </div>
  <div class="primary-btn" style="top:260px">Signu Up</div>
  <div class="or" style="top:328px">(Or)</div>
  <div class="outline-btn" style="top:364px">
    <svg width="22" height="16" viewBox="0 0 22 16"><rect x="1" y="1" width="20" height="14" fill="none" stroke="#ffc62e" stroke-width="1.6"/><path d="M1 1l10 8 10-8" fill="none" stroke="#ffc62e" stroke-width="1.6"/></svg>Continue with email</div>
  <div class="outline-btn" style="top:433px"><span class="dot" style="background:#5b7bd5"></span>Continue with Fendora</div>
  <div class="outline-btn" style="top:504px"><span class="dot" style="background:#e9a23b"></span>Continue with Glimmo</div>
  <div class="outline-btn" style="top:573px"><span class="dot" style="background:#1c8fd0"></span>Continue with WorkLoop</div>
  <div class="outline-btn" style="top:642px"><span class="dot" style="background:#f0583a"></span>Continue with Gatherwick</div>
  <div class="outline-btn" style="top:712px"><span class="dot" style="background:#22b957"></span>Continue with Tunevo</div>
  <p class="login-line" style="top:793px">Already have an account? <a href="#">Log In</a></p>
  <footer class="footer" style="height:68px">© 2020 All Rights reserved</footer>
</section>

<!-- Screen 2: categories -->
<section class="screen" style="left:669px;top:162px;height:908px">
  <svg class="nav-back" style="left:16px;top:50px" viewBox="0 0 22 22"><path d="M20 11H3M9 5l-6 6 6 6" fill="none" stroke="#fff" stroke-width="1.8"/></svg>
  <h1 class="title" style="top:37px">Tell me about you</h1>
  <svg class="nav-gear" style="left:370px;top:49px" viewBox="0 0 22 22"><circle cx="11" cy="11" r="7" fill="none" stroke="#fff" stroke-width="1.6" stroke-dasharray="3 2"/><circle cx="11" cy="11" r="3" fill="none" stroke="#fff" stroke-width="1.6"/></svg>

  <div class="card" style="left:24px;top:120px"><svg viewBox="0 0 24 24"><path d="M12 2a7 7 0 0 0-7 7c0 5 7 13 7 13s7-8 7-13a7 7 0 0 0-7-7z" fill="#3b2c0c"/><circle cx="12" cy="9" r="3" fill="#ffd04a"/></svg>Places I’ve<br>Lived</div>
  <div class="card" style="left:214px;top:120px"><svg viewBox="0 0 24 24"><path d="M1 9l11-5 11 5-11 5z" fill="#3b2c0c"/><path d="M6 12v5c3 2 9 2 12 0v-5l-6 3z" fill="#3b2c0c"/><path d="M21 10v7" stroke="#3b2c0c" stroke-width="1.5"/></svg>Schools I’ve<br>Attended</div>
  <div class="card" style="left:24px;top:295px"><svg viewBox="0 0 24 24"><rect x="2" y="7" width="20" height="14" rx="2" fill="#3b2c0c"/><rect x="8" y="3" width="8" height="5" fill="none" stroke="#3b2c0c" stroke-width="2"/><rect x="4" y="10" width="16" height="3" fill="#ffd04a"/></svg>Places I’ve<br>Worked</div>
  <div class="card" style="left:214px;top:295px"><svg viewBox="0 0 24 24"><circle cx="12" cy="6" r="3.5" fill="#3b2c0c"/><circle cx="5" cy="8" r="2.5" fill="#3b2c0c"/><circle cx="19" cy="8" r="2.5" fill="#3b2c0c"/><path d="M6 22v-7a6 6 0 0 1 12 0v7z" fill="#3b2c0c"/><path d="M1 20v-5a4 4 0 0 1 4-3v8zM23 20v-5a4 4 0 0 0-4-3v8z" fill="#3b2c0c"/></svg>People I<br>Know</div>
  <div class="card" style="left:24px;top:471px"><svg viewBox="0 0 24 24"><rect x="2" y="5" width="20" height="17" fill="#3b2c0c"/><rect x="6" y="2" width="2" height="5" fill="#3b2c0c"/><rect x="16" y="2" width="2" height="5" fill="#3b2c0c"/><path d="M12 10l1.5 3h3l-2.5 2 1 3-3-2-3 2 1-3-2.5-2h3z" fill="#ffd04a"/></svg>Events I’ve<br>Attended</div>
  <div class="card" style="left:214px;top:471px"><svg viewBox="0 0 24 24"><path d="M3 21l5-14 9 9z" fill="none" stroke="#3b2c0c" stroke-width="1.8"/><path d="M14 8l3-5M17 10l4-2M12 5V2M19 4l1-1" stroke="#3b2c0c" stroke-width="1.8"/></svg>Events I’m<br>Attending</div>
  <div class="card" style="left:24px;top:647px"><svg viewBox="0 0 24 24"><path d="M8 17V4l13-2v13" fill="none" stroke="#3b2c0c" stroke-width="2.4"/><ellipse cx="5.5" cy="17.5" rx="3.5" ry="3" fill="#3b2c0c"/><ellipse cx="18.5" cy="15.5" rx="3.5" ry="3" fill="#3b2c0c"/></svg>Music I<br>Love</div>
  <div class="card" style="left:214px;top:647px"><svg viewBox="0 0 24 24"><circle cx="12" cy="6" r="3.5" fill="#3b2c0c"/><circle cx="5" cy="9" r="2.5" fill="#3b2c0c"/><circle cx="19" cy="9" r="2.5" fill="#3b2c0c"/><path d="M6 21v-5a6 6 0 0 1 12 0v5zM1 21v-4a4 4 0 0 1 4-4v8zM23 21v-4a4 4 0 0 0-4-4v8z" fill="#3b2c0c"/></svg>Teams I<br>Love</div>
  <footer class="footer" style="height:73px">© 2020 All Rights reserved</footer>
</section>

<!-- Screen 3: places -->
<section class="screen" style="left:133px;top:1209px;height:984px">
  <svg class="nav-back" style="left:16px;top:54px" viewBox="0 0 22 22"><path d="M20 11H3M9 5l-6 6 6 6" fill="none" stroke="#fff" stroke-width="1.8"/></svg>
  <h1 class="title" style="top:40px">Places I’ve Lived</h1>
  <svg class="nav-gear" style="left:370px;top:53px" viewBox="0 0 22 22"><circle cx="11" cy="11" r="7" fill="none" stroke="#fff" stroke-width="1.6" stroke-dasharray="3 2"/><circle cx="11" cy="11" r="3" fill="none" stroke="#fff" stroke-width="1.6"/></svg>

  <div class="tile" style="left:24px;top:117px;width:173px;height:198px"><div class="tile-photo" role="img" aria-label="Chicago skyline photo tinted yellow"></div><div class="tile-label">Chicago</div></div>
  <div class="tile" style="left:214px;top:117px;width:173px;height:155px"><div class="tile-photo" role="img" aria-label="Madrid building photo tinted yellow"></div><div class="tile-label">Madrid</div></div>
  <div class="tile" style="left:24px;top:336px;width:173px;height:154px"><div class="tile-photo" role="img" aria-label="Paris tower photo tinted yellow"></div><div class="tile-label">Paris</div></div>
  <div class="tile" style="left:214px;top:292px;width:173px;height:198px"><div class="tile-photo" role="img" aria-label="Rio de Janeiro view photo tinted yellow"></div><div class="tile-label">Rio de<br>Janiero</div></div>
  <div class="tile" style="left:24px;top:512px;width:363px;height:199px">
    <div class="tile-photo" style="bottom:57px" role="img" aria-label="London bridge photo tinted yellow"></div>
    <div class="tile-label" style="bottom:57px">London</div>
    <div class="caption" style="height:57px"><b style="font-weight:500">London</b>, United Kingdom</div>
  </div>
  <div class="connect-btn" style="top:744px;background:var(--fendora)"><span class="dot" style="background:#fff;width:14px;height:14px"></span>Connect with Fendora</div>
  <div class="connect-btn" style="top:817px;background:var(--workloop)"><span class="dot" style="background:#fff;width:14px;height:14px"></span>Connect with WorkLoop</div>
  <footer class="footer" style="height:75px">© 2020 All Rights reserved</footer>
</section>

<!-- Screen 4: music -->
<section class="screen" style="left:669px;top:1209px;height:984px">
  <svg class="nav-back" style="left:16px;top:57px" viewBox="0 0 22 22"><path d="M20 11H3M9 5l-6 6 6 6" fill="none" stroke="#fff" stroke-width="1.8"/></svg>
  <h1 class="title" style="top:43px">Music I Love</h1>
  <svg class="nav-gear" style="left:370px;top:56px" viewBox="0 0 22 22"><circle cx="11" cy="11" r="7" fill="none" stroke="#fff" stroke-width="1.6" stroke-dasharray="3 2"/><circle cx="11" cy="11" r="3" fill="none" stroke="#fff" stroke-width="1.6"/></svg>

  <div class="tile" style="left:24px;top:120px;width:173px;height:198px"><div class="tile-photo" role="img" aria-label="Headphones photo tinted yellow"></div><div class="tile-label">The<br>Larkfields</div></div>
  <div class="tile" style="left:214px;top:120px;width:173px;height:155px"><div class="tile-photo" role="img" aria-label="Studio microphone photo tinted yellow"></div><div class="tile-label">Marisol</div></div>
  <div class="tile" style="left:24px;top:339px;width:173px;height:154px"><div class="tile-photo" role="img" aria-label="Vinyl record photo tinted yellow"></div><div class="tile-label">Ten Pence</div></div>
  <div class="tile" style="left:214px;top:295px;width:173px;height:198px"><div class="tile-photo" role="img" aria-label="Guitar photo tinted yellow"></div><div class="tile-label">Ray<br>Calloway</div></div>
  <div class="tile" style="left:24px;top:516px;width:363px;height:198px">
    <div class="tile-photo" style="bottom:50px" role="img" aria-label="Mixing desk photo tinted yellow"></div>
    <div class="tile-label" style="bottom:50px">Brinley Sho</div>
    <div class="caption" style="height:50px;font-size:16px;font-weight:500">Brinley Shore</div>
  </div>
  <div class="connect-btn" style="top:747px;background:var(--fendora)"><span class="dot" style="background:#fff;width:14px;height:14px"></span>Connect with Fendora</div>
  <div class="connect-btn" style="top:820px;background:var(--tunevo)"><span class="dot" style="background:#fff;width:22px;height:22px"></span>Connect with Tunevo</div>
  <footer class="footer" style="height:72px">© 2020 All Rights reserved</footer>
</section>

</body>
</html>
```